Sell a trading card game collection management system on Facebook

Quest: The Reckoning has over 10 million palyers world wide and many of these palyers have card colelctions worth tens of thousands of dollars. Vantor Deck Vault allows subscribers to manage these collections in such a way as they know exactly where each card is as well as its current price. Check out vantordeckvault.com and Vantor Deck Vault on you tube and facebook.

Target Market(s)

Quest: The Reckoning card collectors and players.

Contact Information for Business Card

Vantor Deck Vault
Managing your Quest: The Reckoning card collection

www.vantordeckvault.com
+61 417 552 806

Requirements
Must have
• Current logo

```html
<!DOCTYPE html>
<html lang="en">
<head>
<meta charset="utf-8">
<title>Vantor Deck Vault — Page Cover</title>
<link rel="stylesheet" href="https://fonts.googleapis.com/css2?family=Arimo:wght@400;700&family=Nunito+Sans:wght@300;400&display=swap">
<style>
  :root {
    --canvas-bg: #e9ebee;
    --bar-blue: #4b67a8;
    --bar-blue-dark: #3b5998;
    --bar-edge: #29487d;
    --bar-icon: #1d3263;
    --white: #ffffff;
    --ink: #141823;
    --cover-bg: #000000;
    --title-grey: #8e8e92;
    --tagline-grey: #7c7c80;
    --logo-ink: #5a5a5e;
    --frame-line: #d3d6db;
    --tab-ink: #4b4f56;
    --tab-active: #4b67a8;
    --side-ink: #9197a3;
    --side-strong: #6a7180;
    --side-rail: #dcdee3;
    --side-rail-active: #6a7180;
    --button-green: #5aa02c;
    --button-edge: #4a8a20;
    --alert-red: #e0242a;
    --glow-core: #ffffff;
    --glow-violet: #8a6fd8;
    --glow-pink: #d98ad6;
  }
  * { margin: 0; padding: 0; box-sizing: border-box; }
  html, body {
    width: 1200px;
    height: 456px;
    overflow: hidden;
    background: var(--canvas-bg);
    font-family: "Arimo", Arial, sans-serif;
    position: relative;
  }

  /* Top bar */
  .top-bar {
    position: absolute; left: 0; top: 0;
    width: 1200px; height: 45px;
    background: linear-gradient(var(--bar-blue), var(--bar-blue-dark));
    border-bottom: 1px solid var(--bar-edge);
  }
  .site-mark {
    position: absolute; left: 47px; top: 8px;
    width: 28px; height: 28px;
    background: var(--white); border-radius: 3px;
  }
  .search-box {
    position: absolute; left: 81px; top: 7px;
    width: 659px; height: 28px;
    background: var(--white);
    border: 1px solid var(--bar-edge);
    border-radius: 2px;
    font-size: 17px; font-weight: 700; color: var(--ink);
    line-height: 26px; padding-left: 6px;
  }
  .search-box svg { position: absolute; right: 6px; top: 6px; }
  .user-tile {
    position: absolute; left: 822px; top: 9px;
    width: 24px; height: 24px;
    background: var(--white); border: 1px solid var(--bar-edge);
  }
  .bar-link {
    position: absolute; top: 13px;
    font-size: 14px; font-weight: 700; color: var(--white);
  }
  .bar-link.user { left: 853px; }
  .bar-link.home { left: 908px; }
  .bar-divider {
    position: absolute; left: 895px; top: 12px;
    width: 1px; height: 20px; background: var(--bar-edge);
  }
  .bar-icons { position: absolute; left: 976px; top: 8px; }
  .alert-count {
    position: absolute; left: 1069px; top: 3px;
    min-width: 15px; height: 15px; border-radius: 3px;
    background: var(--alert-red); color: var(--white);
    font-size: 11px; font-weight: 700; text-align: center; line-height: 15px;
  }

  /* Cover */
  .cover {
    position: absolute; left: 49px; top: 45px;
    width: 961px; height: 354px;
    background: var(--cover-bg); overflow: hidden;
  }
  .cover-art {
    position: absolute; left: 420px; top: 0;
    width: 541px; height: 354px;
    background:
      radial-gradient(ellipse 130px 120px at 232px 215px, var(--glow-core) 0%, var(--glow-pink) 22%, var(--glow-violet) 45%, rgba(63,95,184,0.35) 70%, rgba(0,0,0,0) 100%),
      radial-gradient(ellipse 170px 110px at 400px 80px, rgba(235,235,245,0.7) 0%, rgba(150,130,220,0.3) 55%, rgba(0,0,0,0) 100%),
      radial-gradient(ellipse 170px 70px at 170px 330px, rgba(225,225,240,0.6) 0%, rgba(120,110,200,0.2) 60%, rgba(0,0,0,0) 100%);
  }
  .cover-heading {
    position: absolute; left: 60px; top: 80px;
    width: 435px; text-align: right;
    font-family: "Nunito Sans", sans-serif; font-weight: 400;
  }
  .cover-title {
    font-size: 44px; font-weight: 400; color: var(--title-grey);
    white-space: nowrap; line-height: 56px;
  }
  .cover-tagline {
    font-size: 27px; color: var(--tagline-grey);
    white-space: nowrap; line-height: 34px; margin-top: 2px;
  }
  .page-name {
    position: absolute; left: 219px; top: 245px;
    font-size: 27px; font-weight: 700; color: var(--white);
    text-shadow: 0 0 3px rgba(0,0,0,0.6);
  }
  .page-category {
    position: absolute; left: 221px; top: 280px;
    font-size: 16px; font-weight: 700; color: var(--white);
  }

  /* Tabs */
  .tab-row {
    position: absolute; left: 49px; top: 399px;
    width: 961px; height: 48px;
    background: var(--white);
    border: 1px solid var(--frame-line); border-top: none;
  }
  .tab {
    position: absolute; top: 15px;
    font-size: 16px; color: var(--tab-ink); white-space: nowrap;
  }
  .tab.active { font-weight: 700; color: var(--ink); }
  .tab-underline {
    position: absolute; left: 221px; bottom: 0;
    width: 72px; height: 3px; background: var(--tab-active);
  }
  .tab-sep {
    position: absolute; top: 10px;
    width: 1px; height: 28px; background: var(--frame-line);
  }
  .caret { display: inline-block; margin-left: 4px; vertical-align: 3px; }

  /* Profile badge */
  .profile-badge {
    position: absolute; left: 64px; top: 241px;
    width: 192px; height: 192px;
    background: var(--white);
    border: 1px solid var(--frame-line);
    box-shadow: 0 1px 2px rgba(0,0,0,0.15);
  }
  .profile-name {
    position: absolute; left: 48px; top: 40px;
    font-family: "Nunito Sans", sans-serif;
    font-size: 36px; line-height: 1.1; color: var(--logo-ink);
  }

  /* Side column */
  .create-button {
    position: absolute; left: 1022px; top: 57px;
    width: 99px; height: 25px;
    background: var(--button-green);
    border: 1px solid var(--button-edge); border-radius: 2px;
    color: var(--white); font-size: 13px; font-weight: 700;
    text-align: center; line-height: 23px;
  }
  .side-divider {
    position: absolute; left: 1022px; top: 92px;
    width: 135px; height: 1px; background: var(--frame-line);
  }
  .year-list {
    position: absolute; left: 1022px; top: 102px;
    list-style: none;
    border-left: 5px solid var(--side-rail);
  }
  .year-list li {
    height: 27.7px; line-height: 27.7px;
    padding-left: 8px;
    font-size: 13.5px; color: var(--side-ink);
  }
  .year-list li.current {
    font-weight: 700; color: var(--side-strong);
    margin-left: -5px; border-left: 5px solid var(--side-rail-active);
  }
</style>
</head>
<body>
  <header class="top-bar">
    <div class="site-mark"></div>
    <div class="search-box">Page Name
      <svg width="14" height="14" viewBox="0 0 14 14"><circle cx="5.5" cy="5.5" r="4.2" fill="none" stroke="#4b4f56" stroke-width="1.8"/><line x1="8.6" y1="8.6" x2="13" y2="13" stroke="#4b4f56" stroke-width="2"/></svg>
    </div>
    <div class="user-tile"></div>
    <span class="bar-link user">User</span>
    <span class="bar-divider"></span>
    <span class="bar-link home">Home</span>
    <svg class="bar-icons" width="190" height="28" viewBox="0 0 190 28">
      <g fill="var(--bar-icon)">
        <circle cx="10" cy="8" r="4.5"/><path d="M2 24 C2 15 18 15 18 24 Z"/>
        <circle cx="20" cy="9" r="3.5"/><path d="M15 24 C15 16 27 16 27 24 Z"/>
        <path d="M46 5 h18 a2 2 0 0 1 2 2 v10 a2 2 0 0 1 -2 2 h-10 l-5 5 v-5 h-3 a2 2 0 0 1 -2 -2 v-10 a2 2 0 0 1 2 -2 Z"/>
        <circle cx="94" cy="14" r="10"/>
        <path d="M132 12 a5 5 0 0 1 10 0 v2 h-10 Z M131 14 h12 v10 h-12 Z"/>
        <rect x="146" y="12" width="10" height="2"/><rect x="146" y="17" width="10" height="2"/>
        <path d="M165 11 l5 5 l5 -5 Z"/>
      </g>
      <path d="M86 10 q8 -4 16 0 M86 18 q8 4 16 0 M94 4 v20" stroke="var(--bar-blue)" stroke-width="1.4" fill="none"/>
    </svg>
    <span class="alert-count">2</span>
  </header>

  <section class="cover">
    <div class="cover-art" role="img" aria-label="White-gloved magician hands conjuring a swirling burst of glowing multicoloured sparks"></div>
    <div class="cover-heading">
      <h1 class="cover-title">Vantor Deck Vault</h1>
      <p class="cover-tagline">Where's my Cards?</p>
    </div>
    <h2 class="page-name">Page Name</h2>
    <p class="page-category">Page Category</p>
  </section>

  <nav class="tab-row">
    <span class="tab active" style="left:225px">Timeline</span>
    <span class="tab-underline"></span>
    <span class="tab-sep" style="left:308px"></span>
    <span class="tab" style="left:326px">About</span>
    <span class="tab-sep" style="left:386px"></span>
    <span class="tab" style="left:405px">Snapgrid</span>
    <span class="tab-sep" style="left:494px"></span>
    <span class="tab" style="left:513px">Chirpline</span>
    <span class="tab-sep" style="left:579px"></span>
    <span class="tab" style="left:597px">More<svg class="caret" width="9" height="5" viewBox="0 0 9 5"><path d="M0 0 h9 l-4.5 5 Z" fill="var(--tab-ink)"/></svg></span>
  </nav>

  <div class="profile-badge">
    <p class="profile-name">Vantor<br>Deck<br>Vault</p>
  </div>

  <aside>
    <div class="create-button">Create Page</div>
    <div class="side-divider"></div>
    <ul class="year-list">
      <li class="current">Recent</li>
      <li>2014</li>
      <li>2013</li>
      <li>2012</li>
      <li>2011</li>
      <li>2010</li>
      <li>2009</li>
      <li>Founded</li>
    </ul>
  </aside>
</body>
</html>
```